business card for law firm that reflects the web site -www.MarlaQuentby.com. That is pleasant to read

We need a business card for a small law firm. Your company designed our logo - tree of life - which I can provide to the designers. The card should be on both sides. Use the coloring from the web site (www.MarlaQuentby.com) and logo (I have several formats). I am attaching the logo, but not sure what format to use.

First side name of firm: Law Office of M.K. Quentby, P.A. 4819 West Pallisor, Suite 300, Phoenix, AZ 85016, Phone: 602.555.3841, Fax: 602.555.7290, web site: www.MarlaQuentby.com, email: MQuentby@MarlaQuentby.com.
Marla K. Quentby Bankruptcy and Foreclosure Attorney & Counselor.
Back side (perhaps vertical) the logo and then Notes with lines. At the bottom: Proud to help people and small businesses file for bankruptcy protection. We are a debt relief agency.
Updates

I have several versions of the logo. Will be happy to share whatever you need. Added Sunday, April 3, 2016

Target Market(s)

everyone

Industry/Entity Type

Legal

Contact Information for Business Card

I prefer something unique (rounded edges, design that adopts my web site - www.MarlaQuentby.com.

Font styles to use
Serif

Requirements
Must have
• First side name of firm: Law Office of M.K. Quentby, P.A. 4819 West Pallisor, Suite 300, Phoenix, AZ 85016, Phone: 602.555.3841, Fax: 602.555.7290, web site: www.MarlaQuentby.com, email: MQuentby@MarlaQuentby.com.
• Marla K. Quentby Bankruptcy and Foreclosure Attorney & Counselor.
• Back side (perhaps vertical) the logo and then Notes with lines. At the bottom: Proud to help people and small businesses file for bankruptcy protection. We are a debt relief agency.
• Green and brown colors that reflect the web site: www.MarlaQuentby.com
Should not have
• Type so small that older people cannot read.

```html
<!DOCTYPE html>
<html lang="en">
<head>
<meta charset="utf-8">
<title>Marla K. Quentby – Business Card</title>
<link rel="stylesheet" href="https://fonts.googleapis.com/css2?family=Crimson+Text:ital,wght@0,400;0,600;0,700;1,400&display=swap">
<style>
  :root {
    --backdrop: #d9d6d2;
    --card-brown: #4b2214;
    --emblem-faint: #5a2b1a;
    --emblem-faint-ring: #6a3524;
    --forest-green: #1d4a31;
    --paper-white: #ffffff;
    --ink-brown: #3a1a0e;
    --rule-brown: #6b2c1a;
    --text-light: #f4ece6;
  }
  * { box-sizing: border-box; margin: 0; padding: 0; }
  html, body {
    width: 1200px; height: 873px; overflow: hidden;
    background: var(--backdrop);
    font-family: "Crimson Text", Georgia, serif;
  }
  .sheet { position: relative; width: 1200px; height: 873px; }
  .card {
    position: absolute; left: 290px; width: 620px; height: 355px;
    background: var(--card-brown); overflow: hidden;
    box-shadow: 0 6px 18px rgba(0,0,0,.25);
  }
  .card--front { top: 54px; border-radius: 178px 0 0 178px; }
  .card--back  { top: 464px; border-radius: 0 178px 178px 0; }

  /* Front */
  .emblem {
    position: absolute; top: 12px; left: 12px; width: 331px; height: 331px;
    border-radius: 50%; background: var(--forest-green);
    border: 10px solid var(--paper-white);
    display: flex; align-items: center; justify-content: center;
  }
  .emblem__name {
    color: var(--paper-white); font-size: 34px; font-weight: 600;
    letter-spacing: .02em;
  }
  .name-band {
    position: absolute; left: 330px; right: 0; top: 62px; height: 78px;
    background: var(--paper-white); padding: 8px 0 0 26px;
  }
  .name-band__name {
    color: var(--ink-brown); font-size: 34px; line-height: 1.05; font-weight: 400;
  }
  .name-band__title {
    color: var(--forest-green); font-size: 13.5px; font-style: italic; white-space: nowrap;
  }
  .contact {
    position: absolute; left: 360px; top: 160px; right: 12px;
    color: var(--text-light); font-size: 14.5px; line-height: 1.42;
    list-style: none; white-space: nowrap;
  }

  /* Back */
  .notes {
    position: absolute; left: 0; top: 22px; width: 410px; height: 190px;
    background: var(--paper-white); padding: 34px 140px 0 52px;
  }
  .notes__line {
    height: 1px; background: var(--rule-brown); margin-bottom: 30px;
  }
  .emblem-faint {
    position: absolute; top: 12px; right: 12px; width: 331px; height: 331px;
    border-radius: 50%; background: var(--emblem-faint);
    border: 10px solid var(--emblem-faint-ring);
    display: flex; align-items: center; justify-content: center;
  }
  .emblem-faint__name {
    color: var(--emblem-faint-ring); font-size: 34px; font-weight: 600;
  }
  .mission {
    position: absolute; left: 22px; bottom: 42px; width: 250px;
    color: var(--text-light);
  }
  .mission__lead { font-size: 13.5px; line-height: 1.3; margin-bottom: 8px; }
  .mission__notice { font-size: 19px; font-weight: 700; white-space: nowrap; }
</style>
</head>
<body>
<main class="sheet">
  <section class="card card--front" aria-label="Card front">
    <div class="emblem" role="img" aria-label="Firm emblem">
      <span class="emblem__name">M.K. Quentby</span>
    </div>
    <div class="name-band">
      <h1 class="name-band__name">Marla K. Quentby</h1>
      <p class="name-band__title">Bankruptcy and Foreclosure Attorney &amp; Counselor</p>
    </div>
    <ul class="contact">
      <li>Law Office of M.K. Quentby, P.A.</li>
      <li>4819 West Pallisor, Suite 300</li>
      <li>Larkmont, AZ 85762</li>
      <li>(602) 555.3841 Fax: 602.555.7290</li>
      <li>www.MarlaQuentby.com</li>
      <li>MQuentby@MarlaQuentby.com</li>
    </ul>
  </section>

  <section class="card card--back" aria-label="Card back">
    <div class="notes" aria-label="Notes">
      <div class="notes__line"></div>
      <div class="notes__line"></div>
      <div class="notes__line"></div>
      <div class="notes__line"></div>
      <div class="notes__line"></div>
    </div>
    <div class="emblem-faint" role="img" aria-label="Faint firm emblem">
      <span class="emblem-faint__name">M.K. Quentby</span>
    </div>
    <div class="mission">
      <p class="mission__lead">Proud to help people and small businesses file for bankruptcy protection.</p>
      <p class="mission__notice">We are a debt relief agency.</p>
    </div>
  </section>
</main>
</body>
</html>
```